New Brochure for existing Virtual Reality Amusement Arena

I need a two sided half page brochure for my arcade. it needs to say what we do and what we have to offer. It basically needs to be a paper copy of all the information thats on my website www.kavimo-nix.com
Please check that as it is very informative!
Industry/Entity Type
Entertainment
Colors
Designer to choose colors to be used in the design.
Requirements
Must have
- Color. I have uploaded an old brochure I had made, but now we have a new company and new logo, please make it similar to that. Please pull all pics from my website www.kavimo-nix.com
Should not have
- useless information

```html
<!DOCTYPE html>
<html lang="en">
<head>
<meta charset="utf-8">
<title>Kavimo-Nix Brochure</title>
<link rel="stylesheet" href="https://fonts.googleapis.com/css2?family=Lato:wght@400;700&family=Orbitron:wght@700;900&family=Teko:wght@600&display=swap">
<style>
  :root {
    --ink-dark: #15151f;
    --panel-navy: #1a1a2c;
    --stripe-dark: rgba(22, 20, 40, 0.78);
    --sky-blue: #2f5fae;
    --sky-light: #b8c8e0;
    --gear-red: #8a1d24;
    --band-red: #9b2a3a;
    --glow-teal: #2b4b4f;
    --glow-olive: #5a5a28;
    --text-light: #ffffff;
    --page-bg: #2a2a2a;
  }
  * { box-sizing: border-box; margin: 0; padding: 0; }
  html, body { width: 1200px; height: 789px; overflow: hidden; background: var(--page-bg); }
  .brochure {
    position: relative; width: 1200px; height: 789px; overflow: hidden;
    background: var(--ink-dark); color: var(--text-light);
    font-family: 'Lato', sans-serif;
  }
  .panel { position: absolute; top: 0; width: 600px; height: 789px; }
  .panel-back {
    left: 0;
    background:
      radial-gradient(ellipse 420px 360px at 80px 420px, var(--glow-olive), transparent 70%),
      radial-gradient(ellipse 500px 300px at 120px 120px, var(--glow-teal), transparent 70%),
      radial-gradient(ellipse 260px 300px at 560px 560px, rgba(120,30,40,0.6), transparent 70%),
      var(--panel-navy);
  }
  .panel-front {
    left: 600px;
    background:
      radial-gradient(ellipse 380px 420px at 520px 520px, rgba(140,30,45,0.55), transparent 70%),
      var(--panel-navy);
  }
  .hero-photo {
    position: absolute; left: 250px; top: 0; width: 760px; height: 789px;
    background:
      radial-gradient(ellipse 140px 260px at 370px 300px, rgba(40,45,60,0.9), transparent 75%),
      radial-gradient(ellipse 200px 120px at 380px 720px, var(--sky-light), transparent 70%),
      radial-gradient(ellipse 220px 120px at 680px 250px, var(--gear-red), transparent 70%),
      linear-gradient(180deg, #2c56a2 0%, var(--sky-blue) 55%, #6f8fc4 100%);
    -webkit-mask: linear-gradient(90deg, transparent 0, #000 28%, #000 72%, transparent 100%);
            mask: linear-gradient(90deg, transparent 0, #000 28%, #000 72%, transparent 100%);
  }
  .stripe { position: absolute; top: 0; height: 789px; background: var(--stripe-dark); }
  .stripe-a { left: 420px; width: 120px; }
  .stripe-b { left: 790px; width: 160px; }
  .stripe-c { left: 980px; width: 220px; background: rgba(22,20,40,0.45); }
  .fold { position: absolute; left: 599px; top: 0; width: 2px; height: 789px; background: rgba(0,0,0,0.25); }

  .intro { position: absolute; left: 48px; top: 110px; width: 360px; font-size: 12.5px; line-height: 1.3; }
  .hours-title { position: absolute; left: 48px; top: 180px; font-family: 'Orbitron', sans-serif; font-weight: 900; font-size: 17px; letter-spacing: 1px; }
  .hours { position: absolute; left: 48px; top: 212px; border-collapse: collapse; font-size: 15px; }
  .hours td { padding: 0 0 1px 0; line-height: 1.2; }
  .hours td.day { width: 130px; }

  .brand { display: flex; align-items: center; gap: 14px; }
  .brand-dot { border-radius: 50%; background: var(--text-light); flex: none; }
  .brand-name { font-family: 'Lato', sans-serif; font-weight: 700; letter-spacing: 2px; color: var(--text-light); }
  .brand-back { position: absolute; left: 60px; top: 560px; }
  .brand-back .brand-dot { width: 64px; height: 64px; }
  .brand-back .brand-name { font-size: 34px; }
  .address { position: absolute; left: 60px; top: 648px; font-size: 21px; font-weight: 700; line-height: 1.3; }
  .url-band {
    position: absolute; height: 40px; background: var(--band-red);
    display: flex; align-items: center; justify-content: center;
    font-size: 17px; font-weight: 700; letter-spacing: 0.5px;
  }
  .url-back { left: 0; bottom: 0; width: 400px; }
  .url-front { right: 0; bottom: 150px; width: 260px; font-size: 15px; }

  .brand-front { position: absolute; left: 820px; top: 50px; }
  .brand-front .brand-dot { width: 44px; height: 44px; }
  .brand-front .brand-name { font-size: 24px; }
  .tagline { position: absolute; left: 820px; top: 345px; width: 360px; text-align: right; font-size: 13px; font-weight: 700; line-height: 1.3; }
  .headline { position: absolute; left: 730px; top: 395px; }
  .headline-main { font-family: 'Orbitron', sans-serif; font-weight: 900; font-size: 78px; letter-spacing: 4px; line-height: 1; }
  .headline-sub { font-family: 'Teko', sans-serif; font-weight: 600; font-size: 34px; line-height: 1; text-align: right; margin-top: 4px; letter-spacing: 1px; }
</style>
</head>
<body>
<main class="brochure">
  <section class="panel panel-back"></section>
  <section class="panel panel-front"></section>

  <div class="hero-photo" role="img" aria-label="Photo of a player in a VR headset and haptic vest, arms outstretched, holding a red blaster against a blue sky"></div>
  <div class="stripe stripe-a"></div>
  <div class="stripe stripe-b"></div>
  <div class="stripe stripe-c"></div>
  <div class="fold"></div>

  <p class="intro">Just walk right in. Up to eight people can enter at once and stay to try all our products. A new group comes in every 2 hours. Group and entrance times are as follows</p>
  <h2 class="hours-title">HOURS OF OPERATION</h2>
  <table class="hours">
    <tr><td class="day">Monday</td><td>Closed</td></tr>
    <tr><td class="day">Tuesday</td><td>Closed</td></tr>
    <tr><td class="day">Wednesday</td><td>1PM – 9 PM</td></tr>
    <tr><td class="day">Thursday</td><td>1PM – 9 PM</td></tr>
    <tr><td class="day">Friday</td><td>1PM – 9PM</td></tr>
    <tr><td class="day">Saturday</td><td>11 AM – 9 PM</td></tr>
    <tr><td class="day">Sunday</td><td>11AM – 7PM</td></tr>
  </table>

  <div class="brand brand-back"><span class="brand-dot"></span><span class="brand-name">KAVIMO-NIX</span></div>
  <p class="address">2715 W Caldera Ave,<br>Lumen FL 33690</p>
  <div class="url-band url-back">www.kavimo-nix.com</div>

  <div class="brand brand-front"><span class="brand-dot"></span><span class="brand-name">KAVIMO-NIX</span></div>
  <p class="tagline">A virtual reality amusement park and video game lounge.<br>Incorporating the love of video games with<br>state-of-the-art-tech, this is</p>
  <div class="headline">
    <div class="headline-main">GAMING</div>
    <div class="headline-sub">LIKE YOU'VE NEVER SEEN</div>
  </div>
  <div class="url-band url-front">www.kavimo-nix.com</div>
</main>
</body>
</html>
```